Unique business card design

Boutique coastal hotel suites - in need of clever stand out business card I have uploaded the logo that I had created through brand loft I want something that is clever and stands out from everyone else - 418 Marrowind Lane seldovia Alaska 99528 phone or text 907 -561-8204 www.tidewrenlodgeinn.com

Target Market(s)

Men and woman

Industry/Entity Type

Boutique coastal hotel

Contact Information for Business Card

Tidewren Lodge Harrowby Alaska tidewren_lodge@kelpmail.com

Requirements
Must have
• Classy - clever -bold 907-561-8204 call or text

```html
<!DOCTYPE html>
<html lang="en">
<head>
<meta charset="utf-8">
<title>Tidewren Lodge – Business Card</title>
<link href="https://fonts.googleapis.com/css2?family=Montserrat:wght@400;500;700&display=swap" rel="stylesheet">
<style>
  :root {
    --backdrop: #c9c9c9;
    --cream: #efede7;
    --navy: #344f6a;
    --red: #c0392f;
    --yellow: #f2cf4a;
    --white: #ffffff;
  }
  * { box-sizing: border-box; margin: 0; padding: 0; }
  html, body {
    width: 1200px; height: 788px; overflow: hidden;
    background: var(--backdrop);
    font-family: "Montserrat", sans-serif;
  }
  .sheet {
    width: 1200px; height: 788px;
    display: flex; align-items: center; justify-content: center; gap: 40px;
  }
  .card {
    width: 560px; height: 320px;
    border-radius: 26px;
    overflow: hidden;
    position: relative;
    box-shadow: 0 10px 24px rgba(0,0,0,0.25);
  }

  /* Front */
  .card-front { background: var(--navy); display: flex; flex-direction: column; }
  .front-brand {
    height: 140px; background: var(--cream);
    display: flex; align-items: center; justify-content: center; gap: 14px;
  }
  .brand-mark { width: 22px; height: 22px; background: var(--red); flex: none; }
  .brand-name {
    font-weight: 700; font-size: 34px; letter-spacing: 3px;
    text-transform: uppercase; color: var(--navy); white-space: nowrap;
  }
  .phone-band {
    height: 46px; background: var(--red);
    display: flex; align-items: center; padding-left: 40px;
    color: var(--white); font-weight: 700; font-size: 24px; letter-spacing: 0.5px;
    white-space: nowrap;
  }
  .front-details {
    flex: 1; display: flex; align-items: center; padding: 0 34px;
  }
  .person { width: 190px; text-align: right; padding-right: 20px; flex: none; }
  .person-name { color: var(--yellow); font-weight: 700; font-size: 22px; letter-spacing: 1px; white-space: nowrap; }
  .person-role { color: var(--white); font-weight: 500; font-size: 13px; margin-top: 2px; }
  .divider { width: 1px; height: 90px; background: var(--red); flex: none; }
  .contact {
    padding-left: 22px; color: var(--white);
    font-size: 13px; line-height: 1.55; list-style: none; white-space: nowrap;
  }
  .contact li { display: flex; align-items: center; gap: 6px; }
  .contact svg { width: 11px; height: 11px; flex: none; }

  /* Back */
  .card-back {
    background: var(--navy);
    display: flex; align-items: center; justify-content: center; gap: 16px;
  }
  .card-back .brand-name { color: var(--white); font-size: 40px; }
  .card-back .brand-mark { width: 26px; height: 26px; }
</style>
</head>
<body>
<main class="sheet">
  <section class="card card-front" aria-label="Card front">
    <div class="front-brand">
      <span class="brand-mark"></span>
      <span class="brand-name">Tidewren Lodge</span>
    </div>
    <div class="phone-band">907-561-8204 call or text</div>
    <div class="front-details">
      <div class="person">
        <p class="person-name">DANA REYES</p>
        <p class="person-role">Owner</p>
      </div>
      <div class="divider"></div>
      <ul class="contact">
        <li>418 Marrowind Lane</li>
        <li>Harrowby Alaska 99528</li>
        <li>
          <svg viewBox="0 0 12 12" aria-hidden="true"><rect x="0.5" y="2" width="11" height="8" fill="#c0392f"/><path d="M0.5 2 L6 7 L11.5 2" stroke="#fff" stroke-width="1" fill="none"/></svg>
          tidewren_lodge@kelpmail.com
        </li>
        <li>
          <svg viewBox="0 0 12 12" aria-hidden="true"><circle cx="6" cy="6" r="5.5" fill="#c0392f"/><path d="M0.5 6 H11.5 M6 0.5 C3 3.5 3 8.5 6 11.5 M6 0.5 C9 3.5 9 8.5 6 11.5" stroke="#fff" stroke-width="0.8" fill="none"/></svg>
          www.tidewrenlodgeinn.com
        </li>
      </ul>
    </div>
  </section>

  <section class="card card-back" aria-label="Card back">
    <span class="brand-mark"></span>
    <span class="brand-name">Tidewren Lodge</span>
  </section>
</main>
</body>
</html>
```